Lumen Tide flyer KQ Dive Bonaire

On Bonaire we are working on a Lumen Tide project. Growing corals and placing them on the reef, to keep the reefs healthy. KQ Dive has her own coral tree. We are giving Lumen Tide courses, so people can help us to protect the reef.
We like to have a flyer to sell these courses to our guests.
It needs to be informative and appealing for divers to participate.

Target Market(s)

Divers

Industry/Entity Type

Diving / tourism industry

Font styles to use
Sans Serif

Colors
0054AA
0677BA
7BADD7
CADEEF
E8F1F8
F0912C
F2A743
F7CA91
FBE8D2
FDF5EE

Requirements
Must have
• The pictures we added as attachment
Should not have
• No pictures not from Bonaire

```html
<!DOCTYPE html>
<html lang="en">
<head>
<meta charset="utf-8">
<title>Lumen Tide flyers – KQ Dive Bonaire</title>
<link rel="stylesheet" href="https://fonts.googleapis.com/css2?family=Bebas+Neue&family=Barlow:ital,wght@0,500;1,700&family=Roboto:ital,wght@0,400;1,700&family=Sacramento&display=swap">
<style>
  :root {
    --navy: #0f2033;
    --deep-blue: #0054AA;
    --sky: #5cc6f0;
    --sky-light: #8fd7f4;
    --orange: #F2A743;
    --orange-dark: #F0912C;
    --white: #ffffff;
    --stage: #e4e5e6;
  }
  * { margin: 0; padding: 0; box-sizing: border-box; }
  html, body { width: 1200px; height: 960px; overflow: hidden; }
  body { background: var(--stage); position: relative; font-family: "Roboto", sans-serif; }

  .flyer { position: absolute; top: 198px; width: 440px; height: 570px; overflow: hidden; }

  /* Front flyer */
  .flyer-front { left: 118px; }
  .front-photo {
    position: absolute; inset: 0;
    background: linear-gradient(180deg, #9c9ac4 0%, #7a86ad 25%, #6d6f8a 42%, #8a5a45 62%, #7a4632 80%, #6e4a3c 100%);
  }
  .specialty-line {
    position: absolute; left: 52px; top: 65px;
    font-family: "Bebas Neue", sans-serif; font-size: 23px; color: var(--white); letter-spacing: -0.2px;
    white-space: nowrap;
  }
  .specialty-tag { background: var(--white); color: var(--orange-dark); padding: 0 3px; }
  .headline-help {
    position: absolute; left: 48px; top: 74px;
    font-family: "Bebas Neue", sans-serif; font-size: 238px; line-height: 1; color: var(--orange);
    letter-spacing: -4px;
  }
  .headline-restore {
    position: absolute; left: 54px; top: 222px;
    font-family: "Sacramento", cursive; font-size: 118px; line-height: 1; color: var(--white);
  }
  .headline-reefs {
    position: absolute; left: 54px; top: 320px;
    font-family: "Bebas Neue", sans-serif; font-size: 100px; line-height: 1; color: var(--sky);
    letter-spacing: -1px;
  }
  .brand-mark {
    position: absolute; left: 0; right: 0; top: 438px;
    display: flex; justify-content: center; align-items: center; gap: 6px;
    font-family: "Bebas Neue", sans-serif; font-size: 30px; color: var(--orange);
  }
  .brand-dot { width: 12px; height: 12px; border-radius: 50%; background: var(--sky); }
  .front-intro {
    position: absolute; left: 0; right: 0; top: 494px;
    text-align: center; font-size: 11.2px; line-height: 18px; color: var(--white);
  }
  .front-intro em { font-weight: 700; }
  .hl-orange { color: var(--orange); }
  .hl-blue { color: var(--sky); }

  /* Back flyer */
  .flyer-back {
    left: 633px;
    background: linear-gradient(180deg, var(--sky-light) 0%, #b9e5f8 60%, #ffffff 80%);
  }
  .back-title {
    position: absolute; left: 31px; top: 34px; width: 376px; height: 43px;
    background: var(--orange);
    font-family: "Bebas Neue", sans-serif; font-size: 40px; line-height: 45px; color: var(--navy);
    text-align: center; letter-spacing: -0.3px;
  }
  .photo-strip { position: absolute; top: 92px; left: 31px; display: flex; gap: 9px; }
  .photo-tile { width: 120px; height: 205px; border: 2px solid var(--orange); }
  .tile-coral { background: linear-gradient(180deg, #2a7fb8 0%, #4f8fa8 35%, #a89570 70%, #8a7a5a 100%); }
  .tile-diver { background: linear-gradient(180deg, #6fb3dc 0%, #2f7fc0 40%, #3a8fcc 75%, #9cc9e0 100%); }
  .tile-reef { background: linear-gradient(180deg, #2d8a8a 0%, #4aa19a 40%, #b99a80 70%, #c7a68d 100%); }

  .back-question {
    position: absolute; left: 36px; top: 322px;
    font-family: "Barlow", sans-serif; font-style: italic; font-weight: 700; font-size: 28px; line-height: 32px;
    color: var(--navy);
  }
  .info-list { position: absolute; left: 35px; top: 404px; list-style: none; }
  .info-item {
    font-family: "Barlow", sans-serif; font-weight: 500; font-size: 14px; line-height: 20px; color: var(--navy);
    padding-left: 12px; border-left: 3px solid var(--orange); margin-bottom: 13px;
  }
  .info-item.is-blue { border-left-color: var(--sky); }

  .web-band {
    position: absolute; left: 0; top: 514px; width: 280px; height: 30px;
    background: var(--orange);
    font-family: "Bebas Neue", sans-serif; font-size: 28px; line-height: 32px; color: var(--navy);
    padding-left: 36px;
  }
  .gear-photo { position: absolute; right: 0; bottom: 0; width: 250px; height: 215px; }
</style>
</head>
<body>

<section class="flyer flyer-front">
  <div class="front-photo" role="img" aria-label="Underwater photo of a diver surveying a field of staghorn coral"></div>
  <p class="specialty-line">Lumen Tide Diver Distinctive <span class="specialty-tag">Specialty</span></p>
  <h1 class="headline-help">HELP</h1>
  <p class="headline-restore">restore</p>
  <p class="headline-reefs">OUR REEFS!</p>
  <div class="brand-mark"><span class="brand-dot"></span>KQ Dive</div>
  <p class="front-intro">
    Become an active member in helping restore our reef.<br>
    In <em class="hl-orange">2 days</em> and <em class="hl-blue">3 dives</em> you learn all about the reef of Bonaire.
  </p>
</section>

<section class="flyer flyer-back">
  <h2 class="back-title">Discover Lumen Tide Dive</h2>
  <div class="photo-strip">
    <div class="photo-tile tile-coral" role="img" aria-label="Staghorn coral on the Bonaire reef"></div>
    <div class="photo-tile tile-diver" role="img" aria-label="Diver tending a coral tree in the nursery"></div>
    <div class="photo-tile tile-reef" role="img" aria-label="Elkhorn coral in shallow turquoise water"></div>
  </div>
  <p class="back-question">You want to learn<br>more about our reef?</p>
  <ul class="info-list">
    <li class="info-item">Participate in our Discover<br>Lumen Tide dive!</li>
    <li class="info-item is-blue">In half a day we show you<br>what we do to help our reef.</li>
  </ul>
  <p class="web-band">WWW.KQDIVE.COM</p>
  <svg class="gear-photo" viewBox="0 0 250 215" role="img" aria-label="Scuba tank and dive gear resting on a rock">
    <defs>
      <linearGradient id="rockTone" x1="0" y1="0" x2="0" y2="1">
        <stop offset="0" stop-color="#8a8a84"/>
        <stop offset="1" stop-color="#5e5d58"/>
      </linearGradient>
      <linearGradient id="gearTone" x1="0" y1="0" x2="1" y2="1">
        <stop offset="0" stop-color="#3a3d42"/>
        <stop offset="1" stop-color="#1e2024"/>
      </linearGradient>
    </defs>
    <path d="M60 50 Q120 0 200 10 L250 20 L250 150 L60 150 Z" fill="url(#gearTone)"/>
    <path d="M0 215 Q40 160 110 150 Q180 130 250 125 L250 215 Z" fill="url(#rockTone)"/>
  </svg>
</section>

</body>
</html>
```